Global Weight loss program

we need a business card based in Brooklyn , NY called PeppertonRUN . Mara Dulvik Tenbrook the founder and creator of PeppertonRUN Movement. A business based around nutrition, health, Whole Foods and fitness.

Industry/Entity Type

Food Service

Contact Information for Business Card

Phone number : 718-555-0143
website www.peppertonrun.com
email : mara@peppertonrun.com

Font styles to use
Sans Serif

Requirements
Must have
• logo colors
• green black and gold
Nice to have
• must be simple and sharp.
Should not have
• pictures of items

```html
<!DOCTYPE html>
<html lang="en">
<head>
<meta charset="utf-8">
<title>PeppertonRUN Business Card</title>
<link rel="stylesheet" href="https://fonts.googleapis.com/css2?family=Open+Sans:wght@400;600;700&family=Ubuntu:wght@500&display=swap">
<style>
  :root {
    --backdrop: #cfcfcf;
    --card-white: #ffffff;
    --charcoal: #333333;
    --ink: #3a3a3a;
    --green: #6bb83a;
    --rule: #555555;
  }
  * { margin: 0; padding: 0; box-sizing: border-box; }
  html, body { width: 1200px; height: 1008px; overflow: hidden; }
  body {
    background: var(--backdrop);
    font-family: "Open Sans", Arial, sans-serif;
    position: relative;
  }
  .card { position: absolute; overflow: hidden; }
  .card-front {
    left: 318px; top: 166px; width: 558px; height: 319px;
    background: var(--card-white); color: var(--ink);
  }
  .card-back {
    left: 314px; top: 526px; width: 561px; height: 322px;
    background: var(--charcoal); color: #fff;
  }
  .brand-mark-square {
    position: absolute; width: 26px; height: 26px; background: var(--green);
  }
  .brand-name {
    position: absolute; font-family: "Ubuntu", Arial, sans-serif;
    font-weight: 500; font-size: 38px; letter-spacing: -0.5px; line-height: 1;
    white-space: nowrap;
  }
  .brand-tagline {
    position: absolute; font-size: 10px; letter-spacing: 1.6px; line-height: 1;
    white-space: nowrap;
  }
  .card-front .brand-mark-square { left: 53px; top: 86px; }
  .card-front .brand-name { left: 53px; top: 122px; color: var(--ink); }
  .card-front .brand-tagline { left: 54px; top: 159px; color: #555; }
  .person-name {
    position: absolute; right: 54px; top: 183px;
    color: var(--green); font-weight: 700; font-size: 18px; letter-spacing: 0.3px;
  }
  .title-rule {
    position: absolute; left: 54px; top: 217px; width: 380px; height: 1.5px;
    background: var(--rule);
  }
  .person-title {
    position: absolute; right: 54px; top: 207px; font-size: 16px;
  }
  .contact-list { position: absolute; left: 54px; top: 231px; list-style: none; }
  .contact-list li {
    display: flex; align-items: center; height: 22px; font-size: 16px;
  }
  .contact-list svg { width: 15px; height: 15px; margin-right: 7px; flex: none; }
  .address {
    position: absolute; right: 54px; top: 253px; text-align: right;
    font-size: 16px; line-height: 22px;
  }
  .front-band {
    position: absolute; left: 0; bottom: 0; width: 100%; height: 13px;
    background: var(--charcoal);
  }
  .card-back .brand-lockup {
    position: absolute; left: 0; right: 0; top: 90px; text-align: center;
  }
  .card-back .brand-mark-square { position: static; display: inline-block; }
  .card-back .brand-name {
    position: static; display: block; font-size: 40px; color: #fff; margin-top: 72px;
  }
  .card-back .brand-tagline {
    position: static; display: block; color: #bbb; margin-top: 4px;
  }
  .back-website {
    position: absolute; left: 0; right: 0; top: 277px; text-align: center;
    font-size: 15px; color: #bbb; letter-spacing: 0.5px;
  }
  .back-website b { color: #fff; }
</style>
</head>
<body>
  <section class="card card-front">
    <span class="brand-mark-square"></span>
    <div class="brand-name">PeppertonRUN</div>
    <div class="brand-tagline">Fitness, Nutrition and Health</div>

    <div class="person-name">MARA DULVIK TENBROOK</div>
    <div class="title-rule"></div>
    <div class="person-title">Founder</div>

    <ul class="contact-list">
      <li>
        <svg viewBox="0 0 16 16"><path fill="#6bb83a" d="M3.6 1.2l2.2 2.6-1.3 1.6c.8 2 2.3 3.6 4.3 4.5l1.6-1.3 2.6 2.2-1.2 2.3C7 12.6 3.2 8.8 2.5 3.1z"/></svg>
        718-555-0143
      </li>
      <li>
        <svg viewBox="0 0 16 16"><rect x="1" y="3.5" width="14" height="9" fill="#6bb83a"/><path d="M1 3.5l7 5 7-5M1 12.5l5-4.5M15 12.5l-5-4.5" stroke="#fff" stroke-width="1.2" fill="none"/></svg>
        mara@peppertonrun.com
      </li>
      <li>
        <svg viewBox="0 0 16 16" fill="none" stroke="#6bb83a" stroke-width="1.3"><circle cx="8" cy="8" r="6.5"/><ellipse cx="8" cy="8" rx="3" ry="6.5"/><path d="M1.5 8h13M2.5 5h11M2.5 11h11"/></svg>
        <span>www.<b>peppertonrun</b>.com</span>
      </li>
    </ul>

    <div class="address">Your Address Goes Here<br>Address Line 2</div>
    <div class="front-band"></div>
  </section>

  <section class="card card-back">
    <div class="brand-lockup">
      <span class="brand-mark-square"></span>
      <div class="brand-name" style="margin-top:40px">PeppertonRUN</div>
      <div class="brand-tagline">Fitness, Nutrition and Health</div>
    </div>
    <div class="back-website">www.<b>peppertonrun</b>.com</div>
  </section>
</body>
</html>
```